" É uma loja virtual voltada principalmente para a baunilha natural (Fava Bourbon de Madagascar) mas aberta também para outras especiarias, como pimentas, açafrão, canela e outros temperos... possui produtos naturais, produções artesanais e revenda de alguns produtos industriais com base natural. A maioria é de produtos alimentícios, mas também tem produtos de bem-estar como aromatizadores, incensos, velas e etc. "

```html
<!DOCTYPE html>
<html lang="pt-BR">
<head>
<meta charset="UTF-8">
<title>Fava de Baunilha – Rótulo</title>
<link rel="stylesheet" href="https://fonts.googleapis.com/css2?family=Cormorant+Garamond:wght@500;600&family=Great+Vibes&display=swap">
<style>
  :root {
    --backdrop: #e9e8e6;
    --label-light: #f3ead2;
    --label-mid: #dcc79a;
    --label-deep: #b89a5f;
    --ink: #2a1d12;
    --ink-soft: #4a3726;
    --photo-light: #8a6a4c;
    --photo-dark: #3b2719;
    --band-dark: #3a2616;
    --band-mid: #6b4a2c;
    --gold-text: #e8d3a0;
    --flower-light: #f4ecd9;
    --flower-mid: #d8c193;
    --sticker: #f7f5f0;
    --sticker-edge: #d9d4c8;
  }
  * { margin: 0; padding: 0; box-sizing: border-box; }
  html, body {
    width: 1200px; height: 1200px; overflow: hidden;
    background: var(--backdrop);
  }
  .canvas {
    position: relative; width: 1200px; height: 1200px;
    display: flex; align-items: center; justify-content: center;
  }
  .label {
    position: relative; width: 700px; height: 1050px;
    background: linear-gradient(180deg, var(--label-light) 0%, var(--label-mid) 45%, var(--label-deep) 80%);
    overflow: hidden;
  }
  .flower-illustration {
    position: absolute; left: 230px; top: 90px; width: 240px; height: 120px;
    border-radius: 12px;
    background: radial-gradient(ellipse at center, var(--flower-light) 0%, var(--flower-mid) 100%);
  }
  .title {
    position: absolute; top: 270px; width: 100%; text-align: center;
    font-family: "Cormorant Garamond", serif; font-weight: 500;
    font-size: 66px; line-height: 1; letter-spacing: 1px; color: var(--ink);
  }
  .subtitle {
    position: absolute; top: 345px; width: 100%; text-align: center;
    font-family: "Great Vibes", cursive; font-size: 54px; line-height: 1; color: var(--ink);
  }
  .since {
    position: absolute; top: 420px; width: 100%; text-align: center;
    font-family: "Cormorant Garamond", serif; font-weight: 600;
    font-size: 22px; line-height: 1; color: var(--ink-soft);
  }
  .beans-photo {
    position: absolute; left: 0; top: 470px; width: 100%; height: 230px;
    background: linear-gradient(160deg, var(--photo-light) 0%, var(--photo-dark) 100%);
  }
  .flower-icon {
    position: absolute; right: 60px; top: 480px; width: 40px; height: 40px;
    border-radius: 50%; background: var(--ink);
  }
  .barcode-sticker {
    position: absolute; left: 40px; top: 730px; width: 170px; height: 70px;
    background: var(--sticker); border: 1px solid var(--sticker-edge);
  }
  .net-weight {
    position: absolute; right: 55px; top: 760px;
    font-family: "Cormorant Garamond", serif; font-weight: 600;
    font-size: 22px; line-height: 1; color: var(--ink);
  }
  .brand-band {
    position: absolute; left: 0; bottom: 0; width: 100%; height: 200px;
    background: linear-gradient(180deg, var(--band-mid) 0%, var(--band-dark) 100%);
    display: flex; align-items: center; justify-content: center; gap: 18px;
  }
  .brand-name {
    font-family: "Great Vibes", cursive; font-size: 84px; color: var(--gold-text);
    line-height: 1;
  }
  .brand-dot {
    width: 30px; height: 30px; border-radius: 50%; background: var(--gold-text);
  }
</style>
</head>
<body>
<main class="canvas">
  <section class="label">
    <div class="flower-illustration" role="img" aria-label="Ilustração de flor de baunilha com folhas"></div>
    <h1 class="title">FAVA DE BAUNILHA</h1>
    <p class="subtitle">Bourbon de Madagascar</p>
    <p class="since">Tradição desde 2014</p>
    <div class="beans-photo" role="img" aria-label="Fotografia de favas de baunilha secas"></div>
    <div class="flower-icon" role="img" aria-label="Pequeno ícone de flor"></div>
    <div class="barcode-sticker"></div>
    <p class="net-weight">PESO LÍQ. 250g</p>
    <footer class="brand-band">
      <span class="brand-name">Baunilhar</span>
      <span class="brand-dot"></span>
    </footer>
  </section>
</main>
</body>
</html>
```